Help us redesign PlayVault.net ! 550$ of prizes and job position!

Dear Designers,

Playvault.net is part of a bigger startup which spent the last 5 years doing research & developement.

We built a full software stack for the hosting market, starting from our own virtualization technology to the ecommerce software.
Everything was made either with open source software or with software wrote by us.

We made a HUGE investment to build a great platform which we’re now releasing to the public
Thanks to our flexibility we have an unprecedented number of features that allow us to meet every market demands at an unbelievable price point.

We offer EVERYTHING that a multiplayer server needs in a comprehensive package at a competitive price, without hidden fees or activation costs.

Example of features included for free in each of our products are:

- Preconfigured servers of multiple games;

- Ability to run multiple services and servers at once;

- Voice server;

- Web site with forum and store, ready to be used;

- Databases;

- AntiDDoS Firewall, with hacker protection;

and much much more... Our competition charges extras for such services because they need to license third party software, but we can offer them for free since we built them, and we have full control over the source.

We think we will REVOLUTIONIZE the market, but we also think that our current site design ( http://playvault.net/ )is not up to the task.

-

We already partnered with an agency to remake the layout of our site, and we picked this layout:

http://trovelstudio.com/zenby/parallax.html

This is a general indication of how we want the layout of the new home page to be.

We will have a first splash screen, to welcome our users, and then a sticky menu to help navigate in a long, parallax home page.

The menu must be on 2 levels, first level to navigate the site, and second level to navigate inside the page.

What we are asking you is to rethink the graphic, to interpret it in a multiplayer way.

You can make as many changes as you want, but we don't want a complete overhaul, rather to adapt the design to our needs.

-

Prizes:

Winner: 300$

2 part time or a full time position as designer for us

Merit prizes: 1x. 20$

Best Creative Design: 55$ of products

Best Colorful Design: 55$ of products

Best Minimal Design: 55$ of products

Most Sales-Driving Design: 55$ of products

Most Inspired Design: 55$ of products

Jury Award: 55$ of products

Worst Design: 15$ of products

Target Market(s)

Our target market are 14-24 years old. 75% are male students. They like videogames and would like to take their passion to the next level.

Industry/Entity Type

Investment

Font styles to use
Sans Serif

Colors

Designer to choose colors to be used in the design.

Requirements
Must have
• It should be a redesign/interpretation of our site in a new theme:

http://playvault.net/

We want the parallax design and the general layout of the new design.

We want an easy way to integrate youtube videos in the layout.

You must rethink the graphic to adapt it to our market (multiplayer servers, mostly blockcraze)

We need to explain our products, in a easy and clear way.
Nice to have
• It would be nice to see different types of social content in the page, like facebook posts, twitter feed, youtube feeds, etc
Should not have
• It should not be too bloated, too flashy, too complicated. The idea is to make it lighter and simpler. These are a nice example of how this type of design can be interpret in a minimal way:

http://www.kelvrano.com/
http://finalists.plimzoprize.com

Please avoid infringing any copyright.

```html
<!DOCTYPE html>
<html lang="en">
<head>
<meta charset="utf-8">
<title>PlayVault — Home</title>
<link rel="stylesheet" href="https://fonts.googleapis.com/css2?family=Questrial&display=swap">
<style>
  :root {
    --white: #ffffff;
    --ink: #333333;
    --ink-soft: #666666;
    --ink-faint: #9a9a9a;
    --brand-blue: #2f6fae;
    --stripe: #ececec;
    --stripe-dark: #e2e2e2;
    --nav-bg: #e6e6e6;
    --login-bg: #4a4a4a;
    --band-bg: #f2f2f2;
    --map-grey: #ececec;
    --card-map: #c8c8c8;
    --europe-blue: #6f9cc8;
    --crowd-blue: #3a74ad;
    --crowd-deep: #2b5f94;
    --footer-bg: #222222;
    --footer-text: #8a8a8a;
  }
  * { box-sizing: border-box; margin: 0; padding: 0; }
  html, body { width: 1200px; height: 1188px; overflow: hidden; }
  body {
    position: relative;
    background: var(--white);
    font-family: "Questrial", "Century Gothic", sans-serif;
    color: var(--ink);
  }

  /* Splash */
  .splash { position: absolute; left: 0; top: 0; width: 1200px; height: 423px; overflow: hidden; }
  .splash-stripes { position: absolute; inset: 0; }
  .splash-map {
    position: absolute; left: 218px; top: 30px; width: 700px; height: 355px;
    background: radial-gradient(ellipse at center, var(--map-grey) 0%, #f3f3f3 60%, rgba(255,255,255,0) 75%);
  }
  .splash-copy { position: absolute; left: 451px; top: 140px; }
  .splash-kicker { font-size: 15px; color: var(--ink); }
  .splash-title { font-size: 28px; font-weight: 400; color: var(--ink); margin-top: 4px; letter-spacing: 0.3px; }
  .splash-title span { color: var(--brand-blue); }
  .splash-lead { font-size: 11.5px; line-height: 14px; width: 270px; margin-top: 42px; color: #222; }
  .splash-more { display: flex; align-items: center; gap: 6px; font-size: 7.5px; letter-spacing: 0.4px; margin-top: 26px; color: var(--ink); }

  /* Navigation */
  .main-nav { position: absolute; left: 0; top: 423px; width: 1200px; height: 71px; background: var(--nav-bg); }
  .brand { position: absolute; left: 276px; top: 22px; font-size: 26px; color: var(--ink); letter-spacing: -0.5px; }
  .cart { position: absolute; left: 452px; top: 18px; display: flex; align-items: center; gap: 12px; }
  .cart-icon { width: 34px; height: 34px; border-radius: 50%; background: var(--white); display: flex; align-items: center; justify-content: center; }
  .cart-label { font-size: 8.5px; color: var(--ink-soft); line-height: 10px; text-align: center; }
  .cart-label b { color: var(--brand-blue); font-weight: 400; }
  .nav-links { position: absolute; top: 31px; list-style: none; font-size: 11px; color: var(--ink-soft); }
  .nav-links li { position: absolute; white-space: nowrap; }
  .login { position: absolute; left: 846px; top: 0; width: 86px; height: 71px; background: var(--login-bg); color: var(--white); font-size: 11px; font-weight: 700; display: flex; align-items: center; justify-content: center; }

  /* Intro */
  .intro { position: absolute; left: 0; top: 494px; width: 1200px; height: 195px; text-align: center; }
  .intro-title { font-size: 17px; font-weight: 400; margin-top: 53px; color: var(--ink-faint); }
  .intro-title span { color: var(--brand-blue); }
  .intro-text { width: 512px; margin: 31px auto 0; font-size: 8px; line-height: 13px; color: var(--ink-soft); }

  /* Regions */
  .regions { position: absolute; left: 0; top: 689px; width: 1200px; height: 236px; background: var(--band-bg); }
  .region { position: absolute; top: 52px; width: 209px; height: 148px; background: var(--white); }
  .region-map { position: absolute; left: 20px; top: 14px; width: 169px; height: 80px; border-radius: 30px; background: radial-gradient(ellipse, var(--card-map) 0%, #dedede 55%, rgba(255,255,255,0) 75%); }
  .region--europe { background: var(--europe-blue); }
  .region--europe .region-map { left: 0; top: 0; width: 209px; height: 148px; border-radius: 0; background: linear-gradient(160deg, #7aa5cf 0%, #6892bf 100%); }
  .region-name { position: absolute; left: 0; right: 0; top: 110px; text-align: center; font-size: 17px; color: var(--ink-soft); letter-spacing: 0.3px; }
  .region--europe .region-name { color: var(--white); }

  /* Community */
  .community { position: absolute; left: 0; top: 925px; width: 1200px; height: 212px; }
  .community-bg { position: absolute; inset: 0; background: linear-gradient(180deg, var(--crowd-blue) 0%, var(--crowd-deep) 100%); }
  .community-box { position: absolute; left: 378px; top: 68px; width: 450px; height: 94px; background: rgba(255,255,255,0.35); color: var(--white); font-size: 10.5px; line-height: 13px; text-align: center; padding: 18px 28px 0; }

  /* Footer */
  .site-footer { position: absolute; left: 0; top: 1137px; width: 1200px; height: 51px; background: var(--footer-bg); color: var(--footer-text); font-size: 8px; text-align: center; line-height: 51px; }
</style>
</head>
<body>

<header class="splash">
  <svg class="splash-stripes" width="1200" height="423" viewBox="0 0 1200 423" aria-hidden="true">
    <polygon points="0,0 125,0 0,150" fill="var(--stripe-dark)"/>
    <polygon points="125,0 195,0 0,225 0,150" fill="var(--stripe)"/>
    <polygon points="1200,235 1200,300 1090,423 980,423" fill="var(--stripe)"/>
    <polygon points="1200,300 1200,423 1090,423" fill="var(--stripe-dark)"/>
  </svg>
  <div class="splash-map" role="img" aria-label="Light grey world map"></div>
  <div class="splash-copy">
    <p class="splash-kicker">Welcome To</p>
    <h1 class="splash-title">Play <span>Vault</span></h1>
    <p class="splash-lead">Lorem ipsum dolor sit amet, consectetur adipisicing elit, sed do eiusmod tempor</p>
    <p class="splash-more">LEARN MORE
      <svg width="12" height="6" viewBox="0 0 12 6" aria-hidden="true"><path d="M0 3H11M8 0.5L11 3L8 5.5" stroke="var(--ink)" fill="none" stroke-width="1"/></svg>
    </p>
  </div>
</header>

<nav class="main-nav">
  <div class="brand">PlayVault</div>
  <div class="cart">
    <span class="cart-icon">
      <svg width="14" height="12" viewBox="0 0 14 12" aria-hidden="true"><path d="M0.5 1H3L4.5 8H11.5L13 3H4" stroke="#777" fill="none" stroke-width="1"/><circle cx="5.5" cy="10.5" r="1" fill="#777"/><circle cx="10.5" cy="10.5" r="1" fill="#777"/></svg>
    </span>
    <span class="cart-label">Shopping cart<br><b>(1) Item</b></span>
  </div>
  <ul class="nav-links">
    <li style="left:614px">Home</li>
    <li style="left:673px">Products</li>
    <li style="left:754px">Support</li>
  </ul>
  <a class="login">Login</a>
</nav>

<section class="intro">
  <h2 class="intro-title"><span>Lorem ipsum</span> dolor sit amet</h2>
  <p class="intro-text">Lorem ipsum dolor sit amet, consectetur adipisicing elit, sed do eiusmod tempor incididunt ut labore et dolore magna aliqua. Ut enim ad minim veniam, quis nostrud exercitation ullamco laboris nisi ut aliquip ex ea commodo consequat. Duis aute irure dolor in reprehenderit in voluptate velit esse cillum dolore eu fugiat nulla pariatur. Excepteur sint occaecat cupidatat non proident, sunt in culpa qui officia deserunt mollit anim id est laborum.</p>
</section>

<section class="regions">
  <article class="region region--europe" style="left:277px">
    <div class="region-map" role="img" aria-label="Map of Europe in blue"></div>
    <h3 class="region-name">EUROPE</h3>
  </article>
  <article class="region" style="left:501px">
    <div class="region-map" role="img" aria-label="Grey map of North America"></div>
    <h3 class="region-name">AMERICA</h3>
  </article>
  <article class="region" style="left:723px">
    <div class="region-map" role="img" aria-label="Grey world map"></div>
    <h3 class="region-name">REST OF WORLD</h3>
  </article>
</section>

<section class="community">
  <div class="community-bg" role="img" aria-label="Blue-tinted silhouettes of a group of people standing in a row"></div>
  <p class="community-box">Lorem ipsum dolor sit amet, consectetur adipisicing elit, sed do eiusmod tempor incididunt ut labore et dolore magna aliqua. Ut enim ad minim veniam, quis nostrud exercitation ullamco laboris nisi ut aliquip ex ea commodo consequat. Duis aute irure dolor in reprehenderit runt mollit anim id est laborum.</p>
</section>

<footer class="site-footer">PlayVault.net , an initiative of Tomas Verkalis, Liepų 12, Varnelė, Dalvik district, Lithuania</footer>

</body>
</html>
```